Cocktail Syrup / Mixers. Modern clean professional

Looking to design a line of cocktail syrups. The goal would have it look high end. Flavors include Pina Colada, Blue Hawaiian, Margaretta, and other fruit flavors. Labels should be hip, and modern looking. I attached the coffee blends as an example but would like it to be very different from these.

Target Market(s)

18-30

Industry/Entity Type

Food Production

Font styles to use
Serif
Sans Serif

Colors

Designer to choose colors to be used in the design.

Requirements
Must have
• Logo must be centered with the name of the flavor. The label size is 5" height, 8" wide.
Nice to have
• Fruit or some sort of design including different colors per label.
Should not have
• open to everything

```html
<!DOCTYPE html>
<html lang="en">
<head>
<meta charset="utf-8">
<title>Dapper Pour Cocktail Syrup Labels</title>
<link rel="stylesheet" href="https://fonts.googleapis.com/css2?family=Kaushan+Script&family=Poppins:wght@600&display=swap">
<style>
  :root {
    --canvas: #f4f4f4;
    --label-bg: #ffffff;
    --ink: #1c1c1c;
    --blue-deep: #0f9fd8;
    --blue-light: #6fd3f4;
    --blue-pale: #bfeefb;
    --orange-deep: #e8461c;
    --orange-light: #f7862e;
    --orange-pale: #fbc49a;
  }
  * { box-sizing: border-box; margin: 0; padding: 0; }
  html, body { width: 751px; height: 1200px; overflow: hidden; }
  body { background: var(--canvas); position: relative; }

  .label {
    position: absolute;
    left: 55px;
    width: 640px;
    height: 400px;
    background: var(--label-bg);
    overflow: hidden;
    box-shadow: 0 2px 10px rgba(0,0,0,0.08);
  }
  .label--blue-hawaiian { top: 150px; }
  .label--margarita { top: 650px; }

  .label__fruit {
    position: absolute;
    left: 0; top: 176px;
    width: 640px; height: 100px;
  }
  .label--blue-hawaiian .label__fruit {
    background: linear-gradient(90deg, #3b3f8f 0%, #c8243a 25%, #e2354f 50%, #4d4aa3 75%, #c42b45 100%);
  }
  .label--margarita .label__fruit {
    background: linear-gradient(90deg, #f08a1c 0%, #f6b04a 25%, #ef6d55 50%, #f6c23c 75%, #f28a24 100%);
  }

  .label__bands {
    position: absolute; left: 0; top: 0;
    width: 640px; height: 400px;
  }

  .label__brand {
    position: absolute;
    left: 0; top: 92px; width: 640px;
    display: flex; align-items: center; justify-content: center; gap: 14px;
  }
  .brand__dot {
    width: 26px; height: 26px; border-radius: 50%;
    background: var(--ink);
  }
  .brand__name {
    font-family: "Poppins", sans-serif;
    font-weight: 600;
    font-size: 40px;
    line-height: 1;
    color: var(--ink);
  }

  .label__flavor {
    position: absolute;
    left: 0; top: 284px; width: 640px;
    text-align: center;
    font-family: "Kaushan Script", cursive;
    font-weight: 400;
    font-size: 42px;
    line-height: 1;
    color: var(--ink);
  }
</style>
</head>
<body>

  <section class="label label--blue-hawaiian">
    <div class="label__fruit" role="img" aria-label="Photograph of fresh strawberries, raspberries and blueberries"></div>
    <svg class="label__bands" viewBox="0 0 640 400" aria-hidden="true">
      <path d="M0 0 H640 V18 C460 46 200 50 0 30 Z" fill="var(--blue-deep)"/>
      <path d="M0 30 C200 50 460 46 640 18 V34 C460 58 200 62 0 44 Z" fill="var(--blue-light)"/>
      <path d="M0 176 H640 V190 C460 166 200 166 0 200 Z" fill="var(--label-bg)"/>
      <path d="M0 266 C200 248 440 250 640 264 V276 C440 262 200 260 0 280 Z" fill="var(--blue-light)"/>
      <path d="M0 280 C200 260 440 262 640 276 V400 H0 Z" fill="var(--label-bg)"/>
      <path d="M0 362 C220 350 440 352 640 364 V374 C440 362 220 360 0 372 Z" fill="var(--blue-pale)"/>
      <path d="M0 372 C220 360 440 362 640 374 V400 H0 Z" fill="var(--blue-deep)"/>
    </svg>
    <div class="label__brand">
      <span class="brand__dot"></span>
      <span class="brand__name">Dapper Pour</span>
    </div>
    <h2 class="label__flavor">Blue Hawiian</h2>
  </section>

  <section class="label label--margarita">
    <div class="label__fruit" role="img" aria-label="Photograph of sliced oranges, grapefruit and lemons"></div>
    <svg class="label__bands" viewBox="0 0 640 400" aria-hidden="true">
      <path d="M0 0 H640 V18 C460 46 200 50 0 30 Z" fill="var(--orange-deep)"/>
      <path d="M0 30 C200 50 460 46 640 18 V34 C460 58 200 62 0 44 Z" fill="var(--orange-light)"/>
      <path d="M0 176 H640 V190 C460 166 200 166 0 200 Z" fill="var(--label-bg)"/>
      <path d="M0 266 C200 248 440 250 640 264 V276 C440 262 200 260 0 280 Z" fill="var(--orange-light)"/>
      <path d="M0 280 C200 260 440 262 640 276 V400 H0 Z" fill="var(--label-bg)"/>
      <path d="M0 362 C220 350 440 352 640 364 V374 C440 362 220 360 0 372 Z" fill="var(--orange-pale)"/>
      <path d="M0 372 C220 360 440 362 640 374 V400 H0 Z" fill="var(--orange-deep)"/>
    </svg>
    <div class="label__brand">
      <span class="brand__dot"></span>
      <span class="brand__name">Dapper Pour</span>
    </div>
    <h2 class="label__flavor">Margarita</h2>
  </section>

</body>
</html>
```